Stoneline Benchworks Australia - Pool Flyer

G'day,Stoneline Benchworks Australia sells poolforms (https://www.stonelinebenchworksaustralia.com.au/index.php?route=product/category&path=17_61) The poolforms are reusable forms to pour a seamless concrete pool surround instead of using coping tiles. A much better look, less maintenance, and a modern architectural look .We're going to attend a pool and spa show but it is also about landscaping/surround as well. The forms we do make the concrete surround of a pool instead of tiles. I've put some text in a word doc and pictures as well. Feel free to use any words from our website and use/crop pics as you see fit.Any questions, more than happy to answer. We're thinking an A4 tri-fold flyer but happy for other suggestions as well. We're going to attend the show, speak to exhibitors, and hand them the flyer (and maybe a little promo thing too).

Target Market(s)

The target market is we are going to a pool and spa expo. The exhibitors install pools and do backyard landscaping. The flyer is for them.

Colors

Designer to choose colors to be used in the design.

Requirements
Must have
• The text/description of the poolforms and some of the pictures.
• Finished pictures.
• 1 or 2 of the forms (From the website).
• 1 of the Veil skimmer cap pictures (finished is probably better from the jpg with 3 images. probably best to crop and use 1 of the 3.
• Contact details of the website & email contact of sales@stonelinebenchworksaustralia.com.au + the phone number.

```html
<!DOCTYPE html>
<html lang="en">
<head>
<meta charset="utf-8">
<title>Stoneline Benchworks Australia – Pool Flyer</title>
<link href="https://fonts.googleapis.com/css2?family=Special+Elite&family=Tinos:wght@400;700&family=Open+Sans:wght@400;700;800&display=swap" rel="stylesheet">
<style>
  :root{
    --blue:#4a72c2;
    --blue-deep:#3a5fae;
    --grey:#c4c4c9;
    --grey-light:#e2e2e5;
    --ink:#1f1f24;
    --white:#ffffff;
    --photo-pool:linear-gradient(160deg,#9fb6c9 0%,#4f86c0 45%,#1e4f8f 100%);
    --photo-deck:linear-gradient(150deg,#e9e9ea 0%,#bfc3c8 50%,#6f8fb5 100%);
  }
  *{box-sizing:border-box;margin:0;padding:0}
  html,body{width:842px;height:1200px;overflow:hidden;background:var(--white)}
  body{position:relative;font-family:'Open Sans',Arial,sans-serif;color:var(--ink)}

  .sheet{position:absolute;left:31px;width:780px;overflow:hidden}
  .sheet--outside{top:21px;height:559px;background:var(--white)}
  .sheet--inside{top:607px;height:575px;background:var(--grey)}
  .sheet svg.backdrop{position:absolute;inset:0;width:100%;height:100%}

  .photo{position:absolute;background:var(--photo-pool)}
  .photo--pool-left{left:0;top:0;width:262px;height:268px;border-bottom-right-radius:70px}
  .photo--pool-right{left:518px;top:0;width:262px;height:290px;border-bottom-left-radius:80px;background:linear-gradient(200deg,#2b2b2e 0%,#47688f 40%,#1f5ca8 100%)}

  .about{position:absolute;left:8px;top:290px;width:244px}
  .about h2{font-family:'Open Sans',Arial,sans-serif;font-weight:800;font-size:16px;margin-bottom:4px}
  .about p{font-family:'Tinos',serif;font-weight:700;font-size:10.6px;line-height:13.4px;text-align:justify}

  .headline{position:absolute;left:282px;top:36px;width:240px;font-family:'Special Elite',cursive;color:var(--white);font-size:29px;line-height:40px;letter-spacing:2px;text-transform:uppercase}

  .contact{position:absolute;left:268px;top:398px;width:250px;font-family:'Tinos',serif;font-weight:700;font-size:9.6px;line-height:16px;color:var(--ink)}

  .brand{position:absolute;left:552px;top:318px;display:flex;align-items:center;gap:16px}
  .brand__dot{width:78px;height:78px;border-radius:50%;background:var(--white);flex:none}
  .brand__name{font-family:'Open Sans',Arial,sans-serif;font-weight:400;font-size:12px;letter-spacing:3px;line-height:17px;color:var(--white);text-transform:uppercase;width:130px;padding-top:70px}

  .cta{position:absolute;left:20px;top:20px;width:214px;font-family:'Open Sans',Arial,sans-serif;font-weight:700;font-size:21px;line-height:25px;color:var(--white)}

  .photo--form{left:565px;top:0;width:215px;height:150px;border-bottom-left-radius:60px;background:var(--photo-deck)}

  .panel-box{position:absolute;left:6px;top:256px;width:250px;height:314px;background:var(--blue);border-radius:22px;padding:16px 14px 0 18px}
  .features{position:absolute;left:272px;top:262px;width:244px;padding:0 6px}
  .panel-box h3,.features h3{font-family:'Tinos',serif;font-weight:700;font-size:17px;letter-spacing:1.5px;color:var(--white);margin-bottom:10px}
  .ticks{list-style:none}
  .ticks li{position:relative;padding-left:18px;font-family:'Tinos',serif;font-weight:700;font-size:13px;line-height:15px;color:var(--white);margin-bottom:2px}
  .ticks li svg{position:absolute;left:0;top:3px;width:11px;height:10px}

  .tile{position:absolute;width:86px;height:86px;transform:rotate(45deg);border-radius:12px;border:4px solid var(--white);background:var(--photo-deck)}
  .tile--one{left:662px;top:152px}
  .tile--two{left:694px;top:258px;background:var(--photo-pool)}
  .tile--three{left:656px;top:364px;background:linear-gradient(135deg,#f2f2f2,#9aa3ad)}
  .tile--four{left:690px;top:464px;background:linear-gradient(135deg,#d8d6d2,#5d7fae)}
</style>
</head>
<body>

<section class="sheet sheet--outside">
  <svg class="backdrop" viewBox="0 0 780 559" aria-hidden="true">
    <path d="M262 0 H780 V470 Q780 490 760 490 H560 Q522 490 522 452 V420 Q522 378 480 378 H300 Q262 378 262 340 Z" fill="var(--blue)"/>
    <path d="M0 268 Q140 250 262 310 V559 H0 Z" fill="var(--white)"/>
  </svg>

  <div class="photo photo--pool-left" role="img" aria-label="Photo of a finished pool with a seamless concrete surround"></div>
  <div class="photo photo--pool-right" role="img" aria-label="Photo of a backyard pool at dusk with a concrete pool edge"></div>

  <div class="about">
    <h2>About us</h2>
    <p>Stoneline Benchworks Australia (SBA) is Australia and New Zealands only appointed distributor of the Benchform and Edgeform products from Slabcraft Solutions. We provide an online channel for this patented and award winning 2 Benchform decorative edge forms, concrete stains, sealers, and polishes. The product has been designed to make it easy to quickly create fantastic concrete countertops and poolforms at a lower total cost.</p>
  </div>

  <h1 class="headline">The best seamless pooledge forming system</h1>

  <div class="contact">
    <p>Phone no: &nbsp;1300 472 615</p>
    <p>E-mail: sales@stonelinebenchworksaustralia.com.au</p>
    <p>www.stonelinebenchworksaustralia.com.au</p>
  </div>

  <div class="brand">
    <span class="brand__dot"></span>
    <span class="brand__name">Stoneline Benchworks Australia</span>
  </div>
</section>

<section class="sheet sheet--inside">
  <svg class="backdrop" viewBox="0 0 780 575" aria-hidden="true">
    <path d="M0 0 H250 Q300 0 300 50 V190 Q300 230 260 235 H0 Z" fill="var(--blue)"/>
    <path d="M300 40 Q430 10 560 60 L560 110 Q430 60 300 95 Z" fill="var(--grey-light)"/>
    <path d="M0 230 Q150 210 300 250 V262 Q150 222 0 244 Z" fill="var(--grey-light)"/>
    <path d="M520 575 L780 300 V360 L580 575 Z" fill="var(--blue)" opacity=".55"/>
    <path d="M620 575 L780 410 V460 L670 575 Z" fill="var(--blue)" opacity=".55"/>
    <path d="M540 250 Q600 200 640 160" stroke="var(--grey-light)" stroke-width="14" fill="none"/>
  </svg>

  <p class="cta">Get in touch with us to get your hands on the best pool formwork.</p>

  <div class="photo photo--form" role="img" aria-label="Photo of a curved concrete pool edge formed with the poolforms"></div>

  <div class="panel-box">
    <h3>ADVANTAGES</h3>
    <ul class="ticks">
      <li><svg viewBox="0 0 11 10"><path d="M1 5 L4 8 L10 1" stroke="#fff" stroke-width="2" fill="none"/></svg>Easy to use to create a seamless pooledge</li>
      <li><svg viewBox="0 0 11 10"><path d="M1 5 L4 8 L10 1" stroke="#fff" stroke-width="2" fill="none"/></svg>Forms are reusable and do not add to landfill</li>
      <li><svg viewBox="0 0 11 10"><path d="M1 5 L4 8 L10 1" stroke="#fff" stroke-width="2" fill="none"/></svg>Made from tough PVC</li>
      <li><svg viewBox="0 0 11 10"><path d="M1 5 L4 8 L10 1" stroke="#fff" stroke-width="2" fill="none"/></svg>Forms are both straight and bendable so no problem for any shaped pool</li>
      <li><svg viewBox="0 0 11 10"><path d="M1 5 L4 8 L10 1" stroke="#fff" stroke-width="2" fill="none"/></svg>An average sized pool can be formed up and ready for pouring in 2 hours</li>
    </ul>
  </div>

  <div class="features">
    <h3>FEATURES</h3>
    <ul class="ticks">
      <li><svg viewBox="0 0 11 10"><path d="M1 5 L4 8 L10 1" stroke="#fff" stroke-width="2" fill="none"/></svg>Virtually no maintenance</li>
      <li><svg viewBox="0 0 11 10"><path d="M1 5 L4 8 L10 1" stroke="#fff" stroke-width="2" fill="none"/></svg>Architectural-designed look</li>
      <li><svg viewBox="0 0 11 10"><path d="M1 5 L4 8 L10 1" stroke="#fff" stroke-width="2" fill="none"/></svg>Any Type of Concrete - Honed Aggregate, Exposed Aggregate, Grey or any colour concrete</li>
      <li><svg viewBox="0 0 11 10"><path d="M1 5 L4 8 L10 1" stroke="#fff" stroke-width="2" fill="none"/></svg>Form and pour a seamless concrete pool surround</li>
      <li><svg viewBox="0 0 11 10"><path d="M1 5 L4 8 L10 1" stroke="#fff" stroke-width="2" fill="none"/></svg>Any Type of Pool - Fiberglass and concrete pools</li>
    </ul>
  </div>

  <div class="tile tile--one" role="img" aria-label="Photo of a concrete pool surround with a curved edge"></div>
  <div class="tile tile--two" role="img" aria-label="Photo of a finished pool with concrete coping"></div>
  <div class="tile tile--three" role="img" aria-label="Photo of white PVC pool edge forms"></div>
  <div class="tile tile--four" role="img" aria-label="Photo of a finished veil skimmer cap set in concrete"></div>
</section>

</body>
</html>
```